Rosa Caring Star registered NDIS provider

Quality Care, Endless Support: Your NDIS Journey Starts Here
Rosa Caring Star is a compassionate Disability Support Service based in Liverpool NSW . We will provide you and your loved ones professional care and support that is tailored to your individual needs. We offer approved specialised short to long term disability accommodations, support independent living (SIL), assistance with daily tasks including cleaning, meal preparation and gardening, as well as daily programs and activities that range from personal training, community outings, videogames, table tennis, arts and craft, movies, and so much more!
To learn more about our services, feel free to browse our website to read about our NDIS-related blogs. For more information, get in touch with our friendly staff.
Work with Rosa Caring Star today. You and your loved ones deserve only the best.

ROSA CARING STAR
registered NDIS provider
Our services:
Approved specialised disability accommodations.

Support independent living SIL.

Short term accommodations/tenancy & respite.

Development of daily living & life skills

Overnight care active/non-active

Group/day centre activities

Assist in personal care.

Participation in community

Social and civic activities

Daily personal activities

Household tasks

Lawn mowing

Lifelong learning

Daily activities

Meal preparations

Support coordination

Plan management

Registered NDIS Provider
address 47 Brindle Crescent Liverpool NSW 2170
Phone : 0293416578/0471593824
Email : info@rosacaring.example.com.au
Web: : www.rosacaring.example.com.au
our servises in arabic
الخدمات تشمل
١- مساعدة التنقل .

٢- المشاركة الاجتماعية .

٣- تنمية المهارات الحياتية .

٤- مساعدة الأنشطة الشخصية .

٥- المساعدة في المهام المنزلية .

٦- مبيت (Respite ) وعناية على مدار ٢٤ ساعة .

٧- تطوير كافة المهارات اليومية مثلا تعلم الطبخ والميكاب تطوير المهارات الاجتماعية والحياة اليومية و طرق التنقل الامن مثل الباص و القطار
٨- العناية الشخصية والجسدية .
بإلاضافة الى السفرات الفردية والجماعية لمختلف الاعمار .

٩- بيوت مجهزة للسكن الدائمي لخدمات ذوي الاحتياجات الخاصه مع رعايه على مدار ٢٤ ساعة .

Target Market(s)

Disabilty people they need services from ndis provider which is my company registered company with ndis

Industry/Entity Type

Ndis disability services

Font styles to use
Serif

Colors
59FF00
82FF00
B8FF75
E3FFCB
F4FFEA
A7469A
B969AE
D3A5CF
EDDBEB
F8F0F9

Requirements
Must have
• Ndis logo and nice pictures for peoples with disability age from 9 years to 65 years
Should not have
• Old people

```html
<!DOCTYPE html>
<html lang="en">
<head>
<meta charset="utf-8">
<title>Rosa Caring Star – Registered NDIS Provider</title>
<link rel="stylesheet" href="https://fonts.googleapis.com/css2?family=Poppins:wght@400;500;600;700&display=swap">
<style>
  :root{
    --purple:#723a7c;
    --purple-soft:#ebe5ee;
    --green:#8cc63f;
    --ink:#2f2f36;
    --text:#3b3b42;
    --white:#ffffff;
    --page:#e9e9ea;
  }
  *{box-sizing:border-box;margin:0;padding:0}
  html,body{width:783px;height:1200px;overflow:hidden;background:var(--page)}
  body{font-family:"Poppins",sans-serif;color:var(--text)}
  .flyer{position:relative;width:783px;height:1200px;background:var(--white);overflow:hidden}

  .brand{position:absolute;left:40px;top:40px;display:flex;align-items:center;gap:10px}
  .brand-dot{width:44px;height:44px;border-radius:50%;background:var(--green)}
  .brand-name{font-weight:600;font-size:13px;line-height:1.15;color:var(--purple);width:80px}

  .partner-badge{position:absolute;left:633px;top:36px;width:92px;height:92px;border-radius:50%;background:var(--purple)}

  .green-band{position:absolute;left:0;top:160px;width:783px;height:290px;background:var(--green)}
  .hero-photo{position:absolute;left:64px;top:60px;width:640px;height:390px;border-radius:180px 200px 0 0;
    background:
      radial-gradient(ellipse 45% 55% at 72% 40%, rgba(95,130,181,.85), rgba(95,130,181,0) 70%),
      radial-gradient(ellipse 40% 50% at 30% 62%, rgba(240,196,160,.95), rgba(240,196,160,0) 70%),
      linear-gradient(100deg,#f3d6bf 0%,#eec8a6 40%,#a9bedb 62%,#7c9cc7 100%);
    opacity:.95}

  .headline-band{position:absolute;left:0;top:449px;width:783px;height:187px;background:var(--purple)}
  .headline{position:absolute;left:44px;top:474px;color:var(--white)}
  .headline h1{font-weight:700;font-size:31px;line-height:1.25}
  .headline p{font-weight:500;font-size:17px;margin-top:8px}

  .circle-photo{position:absolute;border-radius:50%;border:4px solid var(--white)}
  .circle-group{left:348px;top:452px;width:160px;height:160px;
    background:radial-gradient(circle at 40% 35%,#b9d49a,#7fa25f 55%,#56743f)}
  .circle-wheel{left:452px;top:412px;width:208px;height:208px;
    background:radial-gradient(circle at 55% 55%,#f0a868,#d9dfe4 55%,#9fb1bf)}
  .circle-family{left:614px;top:440px;width:178px;height:178px;
    background:radial-gradient(circle at 45% 45%,#f1e3d6,#d98a80 55%,#b04a48)}

  .about{position:absolute;left:44px;top:656px;width:350px}
  .section-title{font-weight:700;font-size:19px;color:var(--ink)}
  .section-title span{color:var(--purple)}
  .about p{font-size:13.2px;line-height:19.5px;text-align:justify;margin-top:6px}
  .about p + p{margin-top:18px}
  .registered{position:absolute;left:44px;top:1000px;font-weight:500;font-size:25px;color:var(--purple)}

  .services{position:absolute;left:418px;top:640px;width:346px;height:470px;background:var(--purple-soft)}
  .services .section-title{text-align:center;margin-top:28px}
  .service-grid{display:grid;grid-template-columns:repeat(4,1fr);row-gap:16px;padding:14px 6px 0}
  .service{display:flex;flex-direction:column;align-items:center;text-align:center}
  .service svg{width:30px;height:30px}
  .service span{font-size:6.3px;line-height:1.25;margin-top:5px;color:var(--ink);max-width:80px;height:16px}

  .call-panel{position:absolute;left:0;top:1058px;width:443px;height:142px;background:var(--green);border-radius:0 60px 0 0}
  .call-badge{position:absolute;left:44px;top:1091px;width:88px;height:88px;border-radius:50%;background:var(--purple)}
  .call-title{position:absolute;left:150px;top:1066px;font-weight:700;font-size:19px;color:var(--ink)}
  .call-icon{position:absolute;left:148px;top:1112px}
  .call-numbers{position:absolute;left:205px;top:1100px;font-weight:600;font-size:23.5px;line-height:28px;color:var(--white);letter-spacing:.5px}
  .call-web{position:absolute;left:150px;top:1168px;font-size:11.5px;letter-spacing:2.2px;color:var(--ink)}

  .contact-panel{position:absolute;left:420px;top:1108px;width:363px;height:92px;background:var(--purple);border-radius:40px 0 0 0}
  .contact-list{position:absolute;left:465px;top:1126px;list-style:none;color:var(--white);font-size:12.8px;font-weight:500}
  .contact-list li{display:flex;align-items:center;gap:14px;height:28px}
</style>
</head>
<body>
<main class="flyer">
  <div class="brand">
    <div class="brand-dot"></div>
    <div class="brand-name">ROSA CARING STAR</div>
  </div>
  <div class="partner-badge" aria-hidden="true"></div>

  <div class="green-band"></div>
  <div class="hero-photo" role="img" aria-label="Photo of a support worker helping a young girl with her writing"></div>

  <div class="headline-band"></div>
  <div class="headline">
    <h1>Quality Care,<br>Endless Support</h1>
    <p>Your NDIS Journey Starts Here</p>
  </div>

  <div class="circle-photo circle-group" role="img" aria-label="Photo of a group raising hands together in a park"></div>
  <div class="circle-photo circle-wheel" role="img" aria-label="Photo of a smiling young man in a wheelchair by the waterfront"></div>
  <div class="circle-photo circle-family" role="img" aria-label="Photo of a young woman sharing a happy moment with her carer"></div>

  <section class="about">
    <h2 class="section-title">ABOUT <span>US</span></h2>
    <p>Rosa Caring Star is a compassionate Disability Support Service based in Liverpool NSW. We will provide you and your loved ones professional care and support that is tailored to your individual needs. We offer approved specialised short to long term disability accommodations, support independent living (SIL), assistance with daily tasks including cleaning, meal preparation and gardening, as well as daily programs and activities that range from personal training, community outings, videogames, table tennis, arts and craft, movies, and so much more!</p>
    <p>Work with Rosa Caring Star today. You and your loved ones deserve only the best.</p>
  </section>
  <div class="registered">Registered NDIS Provider</div>

  <section class="services">
    <h2 class="section-title">OUR <span>SERVICES</span></h2>
    <div class="service-grid">
      <div class="service"><svg viewBox="0 0 30 30" fill="none" stroke="#723a7c" stroke-width="1.4"><path d="M4 14 15 5l11 9v12H4z"/><rect x="12" y="17" width="6" height="9"/></svg><span>Approved specialised disability accommodations.</span></div>
      <div class="service"><svg viewBox="0 0 30 30" fill="none" stroke="#723a7c" stroke-width="1.4"><path d="M4 14 15 5l11 9v12H4z"/><circle cx="15" cy="18" r="3"/></svg><span>Support independent living SIL.</span></div>
      <div class="service"><svg viewBox="0 0 30 30" fill="none" stroke="#723a7c" stroke-width="1.4"><path d="M4 14 15 5l11 9v12H4z"/><rect x="11" y="15" width="8" height="6"/></svg><span>Short term accommodations/tenancy &amp; respite.</span></div>
      <div class="service"><svg viewBox="0 0 30 30" fill="none" stroke="#723a7c" stroke-width="1.4"><circle cx="15" cy="10" r="4"/><circle cx="8" cy="18" r="3"/><circle cx="22" cy="18" r="3"/><path d="M15 14v12"/></svg><span>Development of daily living &amp; life skills</span></div>

      <div class="service"><svg viewBox="0 0 30 30" fill="none" stroke="#723a7c" stroke-width="1.4"><circle cx="15" cy="16" r="9"/><path d="M15 11v5l3 3"/></svg><span>Overnight care active/non-active</span></div>
      <div class="service"><svg viewBox="0 0 30 30" fill="none" stroke="#723a7c" stroke-width="1.4"><circle cx="15" cy="15" r="4"/><circle cx="15" cy="5" r="2.5"/><circle cx="15" cy="25" r="2.5"/><circle cx="5" cy="15" r="2.5"/><circle cx="25" cy="15" r="2.5"/></svg><span>Group/day centre activities</span></div>
      <div class="service"><svg viewBox="0 0 30 30" fill="none" stroke="#723a7c" stroke-width="1.4"><rect x="9" y="9" width="9" height="16" rx="2"/><path d="M11 9V5h5v4M18 16h7"/></svg><span>Assist in personal care.</span></div>
      <div class="service"><svg viewBox="0 0 30 30" fill="none" stroke="#723a7c" stroke-width="1.4"><rect x="5" y="5" width="20" height="20" rx="3"/><path d="M10 15h10M15 10v10"/></svg><span>Participation in community</span></div>

      <div class="service"><svg viewBox="0 0 30 30" fill="none" stroke="#723a7c" stroke-width="1.4"><circle cx="11" cy="12" r="4"/><circle cx="20" cy="18" r="4"/><circle cx="11" cy="21" r="2"/></svg><span>Social and civic activities</span></div>
      <div class="service"><svg viewBox="0 0 30 30" fill="none" stroke="#723a7c" stroke-width="1.4"><circle cx="10" cy="10" r="4"/><circle cx="20" cy="10" r="4"/><circle cx="10" cy="20" r="4"/><circle cx="20" cy="20" r="4"/></svg><span>Daily personal activities</span></div>
      <div class="service"><svg viewBox="0 0 30 30" fill="none" stroke="#723a7c" stroke-width="1.4"><path d="M5 14 15 6l10 8v11H5z"/><path d="M10 25v-7h10v7"/></svg><span>Household tasks</span></div>
      <div class="service"><svg viewBox="0 0 30 30" fill="none" stroke="#723a7c" stroke-width="1.4"><path d="M5 20h16l3-6"/><circle cx="9" cy="23" r="2"/><circle cx="19" cy="23" r="2"/><path d="M24 14l2-8"/></svg><span>Lawn mowing</span></div>

      <div class="service"><svg viewBox="0 0 30 30" fill="none" stroke="#723a7c" stroke-width="1.4"><rect x="6" y="6" width="18" height="14" rx="2"/><path d="M10 24h10M15 20v4"/></svg><span>Lifelong learning</span></div>
      <div class="service"><svg viewBox="0 0 30 30" fill="none" stroke="#723a7c" stroke-width="1.4"><rect x="6" y="5" width="18" height="20" rx="2"/><path d="M10 11h10M10 16h10M10 21h6"/></svg><span>Daily activities</span></div>
      <div class="service"><svg viewBox="0 0 30 30" fill="none" stroke="#723a7c" stroke-width="1.4"><path d="M9 5v20M6 5v6h6V5M21 5c-3 0-3 8 0 8v12"/></svg><span>Meal preparations</span></div>
      <div class="service"><svg viewBox="0 0 30 30" fill="none" stroke="#723a7c" stroke-width="1.4"><circle cx="15" cy="10" r="4"/><path d="M6 25c0-6 4-9 9-9s9 3 9 9"/></svg><span>Support coordination</span></div>

      <div class="service"><svg viewBox="0 0 30 30" fill="none" stroke="#723a7c" stroke-width="1.4"><circle cx="12" cy="11" r="5"/><path d="M4 24h14l6-5"/></svg><span>Plan management</span></div>
      <div class="service"><svg viewBox="0 0 30 30" fill="none" stroke="#723a7c" stroke-width="1.4"><circle cx="15" cy="15" r="10"/><circle cx="10.5" cy="15" r="1.3" fill="#723a7c"/><circle cx="15" cy="15" r="1.3" fill="#723a7c"/><circle cx="19.5" cy="15" r="1.3" fill="#723a7c"/></svg><span></span></div>
    </div>
  </section>

  <div class="call-panel"></div>
  <div class="call-badge" aria-hidden="true"></div>
  <div class="call-title">CALL US TODAY!</div>
  <svg class="call-icon" width="36" height="36" viewBox="0 0 36 36" aria-hidden="true">
    <circle cx="18" cy="18" r="17" fill="#2f2f36"/>
    <path d="M13 11c1 0 2 3 2 4s-1.5 1.5-1 2.5 3 3.5 4 4 1.5-1 2.5-1 4 1 4 2-1.5 3-3 3c-5 0-11-6-11-11 0-1.5 1.5-3.5 2.5-3.5z" fill="#fff"/>
  </svg>
  <div class="call-numbers">0293416578<br>0471593824</div>
  <div class="call-web">www.rosacaring.example.com.au</div>

  <div class="contact-panel"></div>
  <ul class="contact-list">
    <li><svg width="12" height="14" viewBox="0 0 12 14" aria-hidden="true"><path d="M6 0a5 5 0 0 1 5 5c0 4-5 9-5 9S1 9 1 5a5 5 0 0 1 5-5z" fill="#fff"/><circle cx="6" cy="5" r="2" fill="#723a7c"/></svg>47 Brindle Crescent Liverpool NSW 2170</li>
    <li><svg width="13" height="10" viewBox="0 0 13 10" aria-hidden="true"><rect width="13" height="10" rx="1" fill="#fff"/><path d="M0.5 1 6.5 6 12.5 1" fill="none" stroke="#723a7c" stroke-width="1.2"/></svg>info@rosacaring.example.com.au</li>
  </ul>
</main>
</body>
</html>
```